Real Estate Entrepreneur needs a business card

I am a real estate entrepreneur, I buy houses for investment purposes, I act as a real estate agent representing buyers and sellers in residential home transactions, I am a contractor that does a wide range of home repairs and construction. I'd like a design that can stick with me through the years as my business grows and morphs to fit any niche I decide to pursue as markets change.

Target Market(s)

Anyone with interest that may be related to real estate.

Industry/Entity Type

Real Estate

Contact Information for Business Card

A card that stands out and doesn't put me in any one box. My business will evolve over time and I need a card that can stay relevant.

Colors

Designer to choose colors to be used in the design.

Requirements
Must have
• Character
Nice to have
• I'm open
Should not have
• Cliche houses and hammers

```html
<!DOCTYPE html>
<html lang="en">
<head>
<meta charset="utf-8">
<title>Haven Keep – Business Card</title>
<link rel="stylesheet" href="https://fonts.googleapis.com/css2?family=Open+Sans:wght@600;700&family=Oswald:wght@300;700&display=swap">
<style>
  :root {
    --plum: #33243d;
    --lavender: #b79fce;
    --alert-red: #f51010;
    --brick: #8e2a25;
    --ink: #111111;
    --paper: #ffffff;
    --stage-light: #cfcfcf;
    --stage-dark: #858585;
    --icon-disc: #dcdcdc;
  }
  * { margin: 0; padding: 0; box-sizing: border-box; }
  html, body { width: 1200px; height: 1200px; overflow: hidden; }
  body {
    position: relative;
    background: radial-gradient(ellipse at 50% 50%, var(--stage-light) 0%, var(--stage-dark) 75%);
    font-family: "Open Sans", sans-serif;
  }
  .card {
    position: absolute;
    width: 916px;
    height: 550px;
    overflow: hidden;
  }
  /* Front */
  .card-front {
    left: 160px; top: 28px;
    background: var(--plum);
    display: flex; align-items: center; justify-content: center;
  }
  .brand {
    display: flex; align-items: center; gap: 12px;
    font-family: "Oswald", sans-serif;
    font-weight: 700;
    text-transform: uppercase;
  }
  .brand-front { color: var(--paper); font-size: 58px; letter-spacing: 1px; margin-top: -30px; }
  .brand-front .brand-dot { width: 70px; height: 70px; border: 3px solid var(--paper); border-radius: 50%; }
  /* Back */
  .card-back { left: 154px; top: 622px; background: var(--paper); }
  .top-band {
    position: absolute; left: 0; top: 0; width: 100%; height: 86px;
    background: var(--plum);
    border-bottom: 10px solid var(--lavender);
    height: 96px;
  }
  .tagline {
    position: absolute; left: 0; right: 0; top: 45px;
    text-align: center;
    color: var(--paper);
    font-weight: 700; font-size: 28px; letter-spacing: 2.6px;
    text-transform: uppercase;
  }
  .services {
    position: absolute; left: 0; right: 0; top: 106px;
    text-align: center;
    color: var(--alert-red);
    font-weight: 700; font-size: 16.5px; letter-spacing: 1.1px;
    text-transform: uppercase;
  }
  .areas {
    position: absolute; left: 0; right: 0; top: 138px;
    text-align: center;
    color: var(--ink);
    font-weight: 700; font-size: 18px; letter-spacing: 2px; line-height: 25px;
    text-transform: uppercase;
  }
  .brand-back { position: absolute; left: 33px; top: 418px; color: var(--brick); font-size: 31px; gap: 6px; }
  .brand-back .brand-dot { width: 44px; height: 44px; border: 2.5px solid var(--brick); border-radius: 50%; }
  .contact-list { position: absolute; left: 448px; top: 386px; list-style: none; }
  .contact-item { display: flex; align-items: center; height: 37.5px; }
  .contact-icon {
    width: 30px; height: 30px; border-radius: 50%;
    background: radial-gradient(circle at 40% 35%, #fff 0%, var(--icon-disc) 70%, #b5b5b5 100%);
    display: flex; align-items: center; justify-content: center;
    margin-right: 12px;
  }
  .contact-text {
    font-family: "Oswald", sans-serif; font-weight: 300;
    font-size: 19px; letter-spacing: 1px; color: var(--ink);
    text-transform: uppercase;
  }
  .contact-text.phone { font-family: "Open Sans", sans-serif; font-weight: 700; font-size: 19px; letter-spacing: 1.6px; }
  .bottom-band { position: absolute; left: 0; bottom: 0; width: 100%; height: 36px; background: var(--plum); }
</style>
</head>
<body>
  <section class="card card-front">
    <div class="brand brand-front"><span class="brand-dot"></span><span>Haven Keep</span></div>
  </section>

  <section class="card card-back">
    <div class="top-band"></div>
    <p class="tagline">Protecting your investment with piece of mind</p>
    <p class="services">House management and house check services watching over fine properties in</p>
    <p class="areas">North Scottsdale,<br>Paradise Valley, Carefree,<br>Fountain Hills<br>and the White Mountains</p>

    <div class="brand brand-back"><span class="brand-dot"></span><span>Haven Keep</span></div>

    <ul class="contact-list">
      <li class="contact-item">
        <span class="contact-icon">
          <svg width="14" height="16" viewBox="0 0 14 16"><rect x="3.5" y="1" width="7" height="14" rx="1.5" fill="none" stroke="#222" stroke-width="1.6"/><rect x="5" y="4" width="4" height="4" fill="#222"/></svg>
        </span>
        <span class="contact-text phone">480-555-0142</span>
      </li>
      <li class="contact-item">
        <span class="contact-icon">
          <svg width="16" height="12" viewBox="0 0 16 12"><rect x="1" y="1" width="14" height="10" fill="none" stroke="#222" stroke-width="1.6"/><path d="M1 1 L8 7 L15 1" fill="none" stroke="#222" stroke-width="1.6"/></svg>
        </span>
        <span class="contact-text">havenkeepaz@example.com</span>
      </li>
      <li class="contact-item">
        <span class="contact-icon">
          <svg width="16" height="15" viewBox="0 0 16 15"><path d="M1 7.5 L8 1.5 L15 7.5" fill="none" stroke="#222" stroke-width="1.8"/><rect x="3.5" y="7" width="9" height="7" fill="#222"/><rect x="7" y="10" width="2" height="4" fill="#fff"/></svg>
        </span>
        <span class="contact-text">Licensed and insured home inspectors AZBOTR #40217</span>
      </li>
    </ul>
    <div class="bottom-band"></div>
  </section>
</body>
</html>
```